依頼詳細
【仕様】
『資格完全攻略 突破 ケアワーカー ノート&ドリル 2014 基礎分野編』『資格完全攻略 突破 ケアワーカー ノート&ドリル 2014 応用分野編』は同じ仕様となります。
・B5(182 × 257 ㎜)
・背幅はおよそ20㎜です(修正有)。
・本文は横書ですので左綴じとなります。
・カバー(表1、表4、背表紙):4C(フルカラー)
・表紙(表1、表4、背表紙):1C
・扉:1C

※表紙・扉のデザインはカバーデザインに基づいたもので、「書名」「編者名」「社名」だけが入っているもので結構です。
記載項目
【デザインについて】
・同資格のための参考書・問題集・ワークブックは類書が数多くあり、なかなか差別化が図れないのが現状です。今回は、「資格受験用テキスト・問題集」によく見られるようなキャッチコピーが踊るデザインではなく、すっきりとした知的かつスマートなデザインを希望します。
・書籍の内容は堅いですが、読者が手に取りやすい親しみやすさも加味してください。
・『要点整理と演習集』のデザインにはとらわれませんし、イラスト等を加えていただいても結構です。
・タイトルの文字についてですが、「社会福祉士」「合格」「2013」「共通科目編」「専門科目編」が目に付くようにしてください。特に「社会福祉士」の文言については100級以上の大きさでお願いをします。
・2つの書籍でデザインに盛り込む内容(文字)が異なります。書名、編者名等のデザインに盛り込む内容(文字)は添付ファイルを参照してください。

その他、ご不明な点は、お気軽にお問い合わせください。
希望イメージ
シンプル 複雑
単色 カラフル
暗い 明るい
日常 高級
遊び心 厳粛
未来的 伝統的
女性的 男性的
希望する色
特になし
納品ファイル
• イラストレーター形式 (.ai)
補足説明
■ 選んだ理由

①従来の弊社の書籍とは違うやわらかいイメージ。
②他社の類書との差別化がはかれるデザイン。
③書籍の内容(テキスト・問題集)がもつ「堅い」イメージをやわらげてくれるデザイン。

■ 提案者全員のお礼・コメント

この度は多くのご提案ありがとうございました。
ご応募くださった皆様の提案はとてもバラエティに富み、素晴らしいものが多く迷いましたが、上記の理由により選定させていただきました。
それぞれの提案に社内では「他の書籍ならこのデザインがいい」といった声もきかれました。今回の書籍では惜しくも採用にいたらなかった提案も違う案件によっては十分に採用される可能性がありました。
今後もこのようなデザインをしていただきたい案件がございます。またの機会にも是非ご応募くださいますようお願いいたします。

```html
<!DOCTYPE html>
<html lang="ja">
<head>
<meta charset="utf-8">
<title>資格完全攻略 突破 ケアワーカー ノート&ドリル 2014 基礎分野編</title>
<link href="https://fonts.googleapis.com/css2?family=Noto+Sans+JP:wght@400;500;700;900&family=Montserrat:wght@700;800&display=swap" rel="stylesheet">
<style>
  :root{
    --paper:#fbf6ea;
    --frame:#f6d3b4;
    --outline:#efb78c;
    --orange:#ec7a2c;
    --red:#d9382b;
    --ink:#3a2a22;
    --muted:#6b5a50;
  }
  *{margin:0;padding:0;box-sizing:border-box}
  html,body{width:849px;height:1200px;overflow:hidden;background:#fff}
  .cover{position:relative;width:849px;height:1200px;background:var(--frame);font-family:"Noto Sans JP",sans-serif;color:var(--ink)}
  .cover__inner{position:absolute;inset:22px;background:var(--paper)}
  .side-word{position:absolute;font-family:"Montserrat",sans-serif;font-weight:800;font-size:128px;letter-spacing:18px;color:transparent;-webkit-text-stroke:2.5px var(--outline);white-space:nowrap;line-height:1}
  .side-word--left{left:30px;top:1150px;transform-origin:0 0;transform:rotate(-90deg)}
  .side-word--right{left:820px;top:60px;transform-origin:0 0;transform:rotate(90deg)}
  .catch{position:absolute;top:38px;left:0;right:0;text-align:center;font-size:20px;font-weight:700;color:var(--ink);line-height:1.45}
  .title-top{position:absolute;top:86px;left:0;right:0;text-align:center;font-size:62px;font-weight:900;letter-spacing:2px}
  .title-main{position:absolute;top:158px;left:222px;display:flex;align-items:center;gap:12px}
  .badge{width:54px;height:54px;border-radius:50%;background:var(--red);color:#fff;font-size:20px;font-weight:900;display:flex;align-items:center;justify-content:center;line-height:1}
  .title-name{font-size:66px;font-weight:900;letter-spacing:1px}
  .title-sub{position:absolute;top:232px;left:0;right:0;text-align:center;font-size:36px;font-weight:700;color:var(--orange);letter-spacing:2px}
  .year{position:absolute;top:262px;left:0;right:0;text-align:center;font-family:"Montserrat",sans-serif;font-weight:800;font-size:112px;letter-spacing:6px;color:var(--ink)}
  .credit{position:absolute;top:388px;left:0;right:0;text-align:center;font-size:15px;font-weight:500;color:var(--muted)}
  .contents{position:absolute;left:420px;top:430px;width:310px;height:620px;border:3px solid var(--orange);background:#fff}
  .contents__head{background:var(--orange);color:#fff;text-align:center;padding:10px 0 8px}
  .contents__title{font-size:32px;font-weight:900;letter-spacing:2px;line-height:1.1}
  .contents__scope{font-size:15px;font-weight:500}
  .contents__list{list-style:none;padding:14px 18px;font-size:16px;line-height:1.95;color:var(--ink)}
  .contents__list li{border-bottom:1px dotted var(--outline)}
  .note{position:absolute;font-size:15px;line-height:1.7;color:var(--ink);font-weight:500}
  .note__tag{display:inline-block;background:var(--orange);color:#fff;font-weight:700;font-size:15px;padding:3px 14px;border-radius:14px;margin-bottom:10px}
  .note--drill{left:118px;top:430px;width:240px}
  .note--drill .note__tag{margin-left:-10px}
  .note--note{left:745px;top:430px;width:90px;font-size:14px}
  .publisher{position:absolute;bottom:44px;left:0;right:0;text-align:center;font-size:17px;font-weight:700;color:var(--ink)}
</style>
</head>
<body>
<div class="cover">
  <div class="cover__inner"></div>
  <div class="side-word side-word--left">DRILL</div>
  <div class="side-word side-word--right">NOTE</div>

  <p class="catch">系統立てた記述で理解度アップ！<br>効果的な学習をサポートする合格力養成テキスト</p>
  <h1>
    <span class="title-top">資格完全攻略</span>
    <span class="title-main"><span class="badge">突破</span><span class="title-name">ケアワーカー</span></span>
    <span class="title-sub">ノート&amp;ドリル</span>
    <span class="year">2014</span>
  </h1>
  <p class="credit">森川 透 監修　ケアワーカー資格研究会 編集</p>

  <div class="note note--drill">
    <span class="note__tag">ドリル</span>
    <p>合格のために必要となる必須の知識を確認するための一問一答（過去問題・オリジナル問題）を大項目ごとに収録。</p>
  </div>
  <div class="note note--note">
    <span class="note__tag">ノート</span>
    <p>学科の出題範囲をカバーし、合格圏内の得点以上を正答するための必修事項を精選してわかりやすく解説。</p>
  </div>

  <section class="contents">
    <div class="contents__head">
      <div class="contents__title">基礎分野編</div>
      <div class="contents__scope">（ケアワーカー＋福祉専門職）</div>
    </div>
    <ul class="contents__list">
      <li>人体の構造と機能及び疾病</li>
      <li>心理学理論と心理的支援</li>
      <li>社会理論と社会システム</li>
      <li>現代社会と福祉</li>
      <li>地域福祉の理論と方法</li>
      <li>福祉行財政と福祉計画</li>
      <li>社会保障</li>
      <li>障害者に対する支援と障害者自立支援制度</li>
      <li>低所得者に対する支援と生活保護制度</li>
      <li>保健医療サービス</li>
      <li>権利擁護と成年後見制度</li>
    </ul>
  </section>

  <p class="publisher">(株)あおば書房</p>
</div>
</body>
</html>
```